Velmor Hub Redesign

velmorhub.com is one of our old, high-traffic multilingual site.

its interface is very old, so we want to redesign it to give a modern, attractive design, with comfortable colors and layout.

beside the current content of the main page we want to add two places for dynamic banners.

The site has an App in iOS and Android, we want an ad in a noticeable place for it.

this ad will be permanent.

the site now has 12 languages, but we may add new languages soon, so design must consider this.

redesign of two internal pages also required:
- the main listing page, example: http://www.velmorhub.info/en/cat/252
- the article view page: http://www.velmorhub.info/en/10323

Reason: want to receive more designs ...

```html
<!DOCTYPE html>
<html lang="en">
<head>
<meta charset="utf-8">
<title>Velmor Hub — Questions &amp; Answers</title>
<link href="https://fonts.googleapis.com/css2?family=Open+Sans:wght@400;600;700&family=Oswald:wght@400;500&family=Archivo+Narrow:wght@700&display=swap" rel="stylesheet">
<style>
:root{
  --sky-1:#e9f4fc;
  --sky-2:#9fd0f0;
  --sky-3:#4fa9e2;
  --cyan:#4fc4e3;
  --cyan-dark:#2aa3c8;
  --navy:#1f4f87;
  --ink:#333a40;
  --green:#59b52c;
  --green-light:#8fd04a;
  --paper:#f2f2ee;
  --panel:#ffffff;
  --row:#f1f1f1;
  --border:#dcdcdc;
  --title-blue:#2e6bb0;
  --gold:#b88a2a;
  --footer:#5ccbe6;
  --footer-bottom:#1d6d8e;
  --orange:#f68b1e;
}
*{box-sizing:border-box;margin:0;padding:0}
html,body{width:785px;height:1200px;overflow:hidden}
body{position:relative;background:var(--paper);font-family:"Open Sans",Arial,sans-serif;color:var(--ink)}
.abs{position:absolute}
/* header */
.site-header{left:0;top:0;width:785px;height:200px;background:linear-gradient(160deg,var(--sky-1) 0%,#cfe8f8 40%,var(--sky-2) 70%,var(--sky-3) 100%)}
.brand{left:106px;top:14px;display:flex;align-items:center;gap:8px}
.brand-dot{width:22px;height:22px;border-radius:50%;background:var(--green-light)}
.brand-name{font-size:26px;font-weight:700;color:var(--green)}
.main-nav{left:370px;top:20px;width:310px;height:22px;background:linear-gradient(#3aa8db,#1f7fb9);border-radius:4px;display:flex;align-items:center;justify-content:space-between;padding-right:10px;font-size:8px;font-weight:600;color:#fff;white-space:nowrap;overflow:hidden}
.main-nav span{line-height:22px}
.main-nav .active{background:#1572aa;border-radius:4px 0 0 4px;padding:0 12px}
.hero-title{left:106px;top:76px;font-size:19px;line-height:22px;color:#2c4a74;font-weight:400}
.hero-title em{font-style:normal;color:var(--gold)}
.hero-text{left:106px;top:126px;width:250px;font-size:8.5px;font-weight:600;line-height:12px;color:#4b5868}
.hero-art{left:440px;top:60px;width:170px;height:115px;border-radius:10px;background:linear-gradient(135deg,#f3ead3,#b89a6a 70%,#6e4a2a)}
.search-tab{left:108px;top:170px;width:252px;height:30px;background:linear-gradient(var(--green-light),var(--green));border-radius:18px 18px 0 0;display:flex;align-items:center;padding-left:30px;gap:6px}
.search-input{width:120px;height:16px;background:#fff;border-radius:2px;font-size:8px;color:#aaa;padding:2px 5px}
.search-btn{height:16px;padding:0 10px;border:1px solid #fff;border-radius:3px;font-size:9px;color:#fff;line-height:14px}
/* language bar */
.lang-bar{left:0;top:200px;width:785px;height:34px;background:linear-gradient(var(--cyan),var(--cyan-dark))}
.lang-list{left:100px;top:200px;height:34px;display:flex;font-size:9px;font-weight:600;color:#fff}
.lang-list span{padding:0 10px;line-height:34px;position:relative}
.lang-list .active{background:#e8e8e8;color:#333}
.lang-list small{position:absolute;left:50%;transform:translateX(-50%);top:9px;font-size:6px;font-weight:400}
/* panels */
.panel{background:var(--panel);border:1px solid var(--border)}
.fatwas{left:100px;top:244px;width:426px;height:366px;padding:8px 6px}
.fatwas-head{display:flex;align-items:center;gap:8px;height:24px;margin-bottom:6px}
.fatwas-head h2{font-size:14px;font-weight:700;color:var(--title-blue)}
.fatwas-head .rule{flex:1;height:1px;background:#ccc}
.pager{display:flex;gap:2px}
.pager i{width:13px;height:13px;background:var(--cyan-dark)}
.fatwa{display:flex;align-items:center;gap:8px;height:44px;margin-bottom:3px;background:var(--row);border-radius:6px;padding:0 60px 0 8px;font-size:10px;line-height:13px;color:#444}
.fatwa-icon{flex:none;width:14px;height:14px;border-radius:50%;background:var(--green)}
.ad-cash{left:533px;top:244px;width:149px;height:366px;padding:4px}
.ad-inner{height:100%;background:linear-gradient(#cfe6f8,#9fcbf0);display:flex;flex-direction:column;align-items:center;font-family:Arial,sans-serif}
.apply{margin-top:6px;width:100px;height:24px;border-radius:12px;background:var(--orange);border:2px solid #fff;color:#fff;font-size:13px;font-weight:700;text-align:center;line-height:20px}
.big{font-family:"Archivo Narrow",Arial,sans-serif;font-size:28px;font-weight:700;color:var(--navy);line-height:28px;text-align:center}
.ad-band{width:100%;background:var(--navy);color:#fff;font-size:9.5px;padding:20px 0 10px 16px;margin:8px 0}
.ad-band p{line-height:12px}
.ad-band b{display:block;text-align:center;margin:10px -16px 0 -16px;font-size:10px}
.ad-band b strong{font-size:13px;display:block}
.topics{left:100px;top:618px;width:426px;height:264px}
.topic{position:absolute;width:142px;text-align:center}
.topic-icon{width:40px;height:34px;margin:0 auto 4px;border-radius:8px}
.topic h3{font-family:"Oswald",sans-serif;font-weight:400;font-size:10.5px;color:var(--title-blue);margin-bottom:4px}
.topic p{font-size:8.5px;line-height:10px;color:#555}
.divider-v{position:absolute;width:1px;background:#e2e2e2}
.divider-h{position:absolute;left:50px;width:330px;height:1px;background:#e2e2e2}
.side{left:533px;width:149px;padding:8px}
.side h2{font-family:"Oswald",sans-serif;font-weight:400;font-size:12px;color:var(--title-blue);border-bottom:1px solid #ddd;padding-bottom:3px}
.side ul{list-style:none}
.side li{display:flex;gap:6px;font-size:7.5px;color:#666;border-bottom:1px solid #eee;padding:4px 0;line-height:9px}
.side li svg{flex:none}
.full{position:absolute;right:8px;bottom:8px;border:1px solid #b5dba0;font-size:7.5px;line-height:10px;color:var(--green);padding:2px 6px}
.finance{left:100px;top:888px;width:426px;height:98px;padding:6px}
.finance-inner{display:flex;height:100%}
.finance-text{width:255px;background:#4d7fbf;color:#fff;font-size:19px;display:flex;align-items:center;padding-left:10px}
.finance-photo{flex:1;background:linear-gradient(#6aa9dc,#a8cbe8 60%,#5a6f85)}
/* footer */
.footer{left:0;top:994px;width:785px;height:168px;background:var(--footer)}
.foot-about{left:106px;top:1014px;width:200px}
.foot-about h2{font-family:"Oswald",sans-serif;font-weight:500;font-size:14px;color:#1d4f7c;margin-bottom:6px}
.foot-about p{font-size:7.5px;line-height:10px;color:#234;margin-bottom:8px}
.social{display:flex;gap:5px}
.social i{width:21px;height:21px;border-radius:50%;background:#1f6fa8}
.social i:nth-child(2),.social i:nth-child(5){background:#c8282b}
.foot-col{top:1024px;font-size:7.5px;color:#0f3c63;line-height:12px}
.foot-col h3{font-family:"Oswald",sans-serif;font-weight:400;font-size:9.5px;color:#1d4f7c;border-bottom:1px solid #89d9ee;padding-bottom:3px;margin-bottom:6px;width:90px}
.store{width:98px;height:32px;background:#111;border:1px solid #888;border-radius:5px;margin-bottom:8px}
.foot-bottom{left:0;top:1162px;width:785px;height:38px;background:var(--footer-bottom);color:#fff;font-size:7.5px;line-height:38px;text-align:right;padding-right:112px}
</style>
</head>
<body>
<header class="abs site-header"></header>
<div class="abs brand"><span class="brand-dot"></span><span class="brand-name">Velmor Hub</span></div>
<nav class="abs main-nav"><span class="active">HOME</span><span>SHOWCASE</span><span>ROOMS</span><span>ABOUT</span><span>GALLERY</span><span>CONTACT</span></nav>
<h1 class="abs hero-title">Are You Looking For Islamic<br><em>Questions Answers?</em></h1>
<p class="abs hero-text">Parturnt monte scetur ravida necluctus rem. Maecenas tris-tiqurci ferode.parturnt monte scetur ravida necluctus rem. Maecenas tristiqurci ferode.</p>
<div class="abs hero-art" role="img" aria-label="Open book resting on a wooden stand"></div>
<div class="abs search-tab"><span class="search-input">SEARCH KEYWORDS</span><span class="search-btn">Search</span></div>

<div class="abs lang-bar"></div>
<div class="abs lang-list">
  <span class="active">English</span><span>中文</span><span>Uygur</span><span>Français</span><span>Español</span><span>日本語</span><span>Indonesian</span><span>Русский<small>New</small></span><span>Turk</span><span>Urdu</span><span>Hindi<small>New</small></span>
</div>

<section class="abs panel fatwas">
  <div class="fatwas-head"><h2>NEW FATWAS</h2><span class="rule"></span><span class="pager"><i></i><i></i><i></i></span></div>
  <div class="fatwa"><span class="fatwa-icon"></span>His mother mistreats his wife and her family.</div>
  <div class="fatwa"><span class="fatwa-icon"></span>Partner took money from the company without his partner's knowledge.</div>
  <div class="fatwa"><span class="fatwa-icon"></span>How can the Qur'an be a miracle for the non-Arabs when it is Arabic and they do not know Arabic?.</div>
  <div class="fatwa"><span class="fatwa-icon"></span>Ruling on offering congratulations at the beginning of the Hijri year.</div>
  <div class="fatwa"><span class="fatwa-icon"></span>His parents think that he does not offer the naafil prayers, but he prays them in secret for fear of showing off. Should he tell them about that?</div>
  <div class="fatwa"><span class="fatwa-icon"></span>The reason why the husband is regarded as superior and is given the role of qawwaam (protector and maintainer).</div>
  <div class="fatwa"><span class="fatwa-icon"></span>Raising Muslim children in the West to have an aversion to pigs.</div>
</section>

<aside class="abs panel ad-cash">
  <div class="ad-inner">
    <div class="apply">Apply Now ›</div>
    <div class="big" style="margin-top:8px">Need<br>Fast<br>Cash?</div>
    <div class="ad-band"><p>● Approval in Seconds</p><p>● No Credit Check</p><p>● High Approval Rate</p><b>Privacy &amp; Security<strong>PROTECTED</strong></b></div>
    <div class="big">Bad<br>Credit<br>OK!</div>
    <div class="apply">Apply Now ›</div>
  </div>
</aside>

<section class="abs panel topics">
  <div class="topic" style="left:0;top:14px"><div class="topic-icon" role="img" aria-label="Group of people icon" style="background:linear-gradient(#7fc2f2,#f2a91e)"></div><h3>Counseling</h3><p>Lorem ipsum dolor sit amet,<br>consectetuer adipiscing elit.<br>Praesent vestibulum</p></div>
  <div class="topic" style="left:142px;top:14px"><div class="topic-icon" role="img" aria-label="Document icon" style="background:linear-gradient(#fff7d8,#f0a824)"></div><h3>Jurisprudence of acts of worship</h3><p>Lorem ipsum dolor sit amet,<br>consectetuer adipiscing elit.<br>Praesent vestibulum</p></div>
  <div class="topic" style="left:284px;top:14px"><div class="topic-icon" role="img" aria-label="Pie chart icon" style="background:linear-gradient(#f7c94a,#2e8fd6)"></div><h3>Jurisprudence of Muslim minorities</h3><p>Lorem ipsum dolor sit amet,<br>consectetuer adipiscing elit.<br>Praesent vestibulum</p></div>
  <div class="divider-h" style="top:126px"></div>
  <div class="topic" style="left:0;top:150px"><div class="topic-icon" role="img" aria-label="Cash box icon" style="background:linear-gradient(#444,#d8b53a)"></div><h3>Contemporary transactions</h3><p>Lorem ipsum dolor sit amet,<br>consectetuer adipiscing elit.<br>Praesent vestibulum</p></div>
  <div class="topic" style="left:142px;top:150px"><div class="topic-icon" role="img" aria-label="Book cover icon" style="background:linear-gradient(#d9a64a,#7a4a1e)"></div><h3>Basic tenets of Faith</h3><p>Lorem ipsum dolor sit amet,<br>consectetuer adipiscing elit.<br>Praesent vestibulum</p></div>
  <div class="topic" style="left:284px;top:150px"><div class="topic-icon" role="img" aria-label="Woman in headscarf icon" style="background:linear-gradient(#ddd,#8a8a8a)"></div><h3>The Muslim Women</h3><p>Lorem ipsum dolor sit amet,<br>consectetuer adipiscing elit.<br>Praesent vestibulum</p></div>
  <div class="divider-v" style="left:142px;top:10px;height:100px"></div>
  <div class="divider-v" style="left:284px;top:10px;height:100px"></div>
  <div class="divider-v" style="left:142px;top:140px;height:104px"></div>
  <div class="divider-v" style="left:284px;top:140px;height:104px"></div>
</section>

<section class="abs panel side" style="top:618px;height:180px">
  <h2>CATEGORIES</h2>
  <ul>
    <li><svg width="9" height="9" viewBox="0 0 9 9"><rect x=".5" y=".5" width="8" height="8" fill="none" stroke="#59b52c"/><path d="M2 4.5l2 2 3.5-4" fill="none" stroke="#59b52c" stroke-width="1.3"/></svg>Basic tenets of faith</li>
    <li><svg width="9" height="9" viewBox="0 0 9 9"><rect x=".5" y=".5" width="8" height="8" fill="none" stroke="#59b52c"/><path d="M2 4.5l2 2 3.5-4" fill="none" stroke="#59b52c" stroke-width="1.3"/></svg>The Quraan and its sciences</li>
    <li><svg width="9" height="9" viewBox="0 0 9 9"><rect x=".5" y=".5" width="8" height="8" fill="none" stroke="#59b52c"/><path d="M2 4.5l2 2 3.5-4" fill="none" stroke="#59b52c" stroke-width="1.3"/></svg>Hadeeth &amp; its Sciences</li>
    <li><svg width="9" height="9" viewBox="0 0 9 9"><rect x=".5" y=".5" width="8" height="8" fill="none" stroke="#59b52c"/><path d="M2 4.5l2 2 3.5-4" fill="none" stroke="#59b52c" stroke-width="1.3"/></svg>Rulings on Jihaad</li>
    <li><svg width="9" height="9" viewBox="0 0 9 9"><rect x=".5" y=".5" width="8" height="8" fill="none" stroke="#59b52c"/><path d="M2 4.5l2 2 3.5-4" fill="none" stroke="#59b52c" stroke-width="1.3"/></svg>Fiqh of the family</li>
    <li><svg width="9" height="9" viewBox="0 0 9 9"><rect x=".5" y=".5" width="8" height="8" fill="none" stroke="#59b52c"/><path d="M2 4.5l2 2 3.5-4" fill="none" stroke="#59b52c" stroke-width="1.3"/></svg>Islamic history and biography</li>
  </ul>
  <span class="full">Full List ›</span>
</section>

<section class="abs panel side" style="top:804px;height:182px">
  <h2>FILES</h2>
  <ul>
    <li><svg width="9" height="9" viewBox="0 0 9 9"><rect x=".5" y=".5" width="8" height="8" fill="none" stroke="#59b52c"/><path d="M2 4.5l2 2 3.5-4" fill="none" stroke="#59b52c" stroke-width="1.3"/></svg>The virtue of fasting 'Ashoora'</li>
    <li><svg width="9" height="9" viewBox="0 0 9 9"><rect x=".5" y=".5" width="8" height="8" fill="none" stroke="#59b52c"/><path d="M2 4.5l2 2 3.5-4" fill="none" stroke="#59b52c" stroke-width="1.3"/></svg>prohibition on songs and music</li>
    <li><svg width="9" height="9" viewBox="0 0 9 9"><rect x=".5" y=".5" width="8" height="8" fill="none" stroke="#59b52c"/><path d="M2 4.5l2 2 3.5-4" fill="none" stroke="#59b52c" stroke-width="1.3"/></svg>Rulings on witchcraft, the evil eye and destructive envy</li>
    <li><svg width="9" height="9" viewBox="0 0 9 9"><rect x=".5" y=".5" width="8" height="8" fill="none" stroke="#59b52c"/><path d="M2 4.5l2 2 3.5-4" fill="none" stroke="#59b52c" stroke-width="1.3"/></svg>Travel and tourism</li>
    <li><svg width="9" height="9" viewBox="0 0 9 9"><rect x=".5" y=".5" width="8" height="8" fill="none" stroke="#59b52c"/><path d="M2 4.5l2 2 3.5-4" fill="none" stroke="#59b52c" stroke-width="1.3"/></svg>Rulings of wiping over socks</li>
    <li><svg width="9" height="9" viewBox="0 0 9 9"><rect x=".5" y=".5" width="8" height="8" fill="none" stroke="#59b52c"/><path d="M2 4.5l2 2 3.5-4" fill="none" stroke="#59b52c" stroke-width="1.3"/></svg>Rulings of Dreams</li>
  </ul>
  <span class="full">Full List ›</span>
</section>

<section class="abs panel finance">
  <div class="finance-inner">
    <div class="finance-text">GLOBAL ISLAMIC FINANCE</div>
    <div class="finance-photo" role="img" aria-label="City skyline with tall towers"></div>
  </div>
</section>

<footer class="abs footer"></footer>
<div class="abs foot-about">
  <h2>About Velmor Hub</h2>
  <p>Lorem ipsum dolor sit amet, consectetuer adipiscing elit. Pra esent vestibulum molestie lacus. Aenean nonummy hendrerit mauris. Phasellus porta. Fusce suscipit varius mi. Cum sociis natoque penatibus et magnis dis parturient montes, nascetur ridiculus mus.</p>
  <p>Nulla dui. Fusce feugiat malesuada odio. Morbi nunc odio, gravida at, cursus nec, luctus a, lorem.</p>
  <div class="social"><i></i><i></i><i></i><i></i><i></i></div>
</div>
<div class="abs foot-col" style="left:362px"><h3>COMPANY</h3>Home<br>About Us<br>Contact Us<br>NewFatwas<br>Privacy Policy<br>Articles &amp; Books<br>Send A Question</div>
<div class="abs foot-col" style="left:457px"><h3>LANGUAGES</h3>中文<br>Uygur<br>Français<br>Español<br>日本語<br>Indonesian<br>Русский new<br>Turkish</div>
<div class="abs foot-col" style="left:550px"><h3>DOWNLOAD APPS</h3><div class="store"></div><div class="store"></div></div>
<div class="abs foot-bottom">© 2013 Website Company Name. All Rights Reserved</div>
</body>
</html>
```